Mardi Gras 2013 Design Project

We have a design with elements that we want to retain. However, we need to take what we have and give it a creative BOOST!

Requirements
Must have
• Colors must stay, "KT" logo must stay,
Copy must remain (except - "Requests Your Presence" and small copy in bottom right corner);
Seal must remain, "9th Annual Velvet Lantern Gala" frame text can be modified but should resemble;
Gotham font to remain
Nice to have
• Any new Mardi Gras element - like a mask or beads - but can not over shadow copy

```html
<!DOCTYPE html>
<html lang="en">
<head>
<meta charset="utf-8">
<title>9th Annual Velvet Lantern Gala</title>
<link rel="stylesheet" href="https://fonts.googleapis.com/css2?family=Montserrat:ital,wght@0,700;0,800;0,900;1,900&display=swap">
<style>
:root{
  --bg-center:#6a93e0;
  --bg-edge:#3b5ea8;
  --orange:#ff7a1c;
  --green:#3dff3a;
  --lavender:#e6e0ff;
  --royal:#1b2ee0;
  --purple:#3a1f86;
  --gold:#c99a1a;
  --ink:#0a0a0a;
  --white:#ffffff;
}
*{margin:0;padding:0;box-sizing:border-box}
html,body{width:928px;height:1200px;overflow:hidden;background:var(--white)}
body{font-family:"Montserrat",Arial,sans-serif}
.invitation{
  position:relative;width:928px;height:1200px;overflow:hidden;
  border:3px solid var(--ink);
  background:radial-gradient(ellipse at 50% 48%,var(--bg-center) 0%,var(--bg-edge) 85%);
}
.invitation > *{position:absolute;line-height:1}
.brand-mark{left:46px;top:38px;font-weight:900;font-size:150px;letter-spacing:-6px;color:var(--purple)}
.host{left:381px;top:144px;font-weight:800;font-size:27px;line-height:34px;color:var(--orange);text-shadow:0 0 4px rgba(255,255,255,.35)}
.request{left:509px;top:232px;font-weight:800;font-size:23px;line-height:30px;color:var(--orange);text-shadow:0 0 4px rgba(255,255,255,.35)}
.edition-number{left:258px;top:200px;font-weight:900;font-style:italic;font-size:270px;letter-spacing:-10px;color:var(--green);text-shadow:0 2px 12px rgba(255,255,255,.55)}
.edition-suffix{left:452px;top:326px;font-weight:900;font-style:italic;font-size:118px;color:var(--green);text-shadow:0 2px 10px rgba(255,255,255,.5)}
.title{font-weight:900;text-shadow:0 3px 10px rgba(255,255,255,.6)}
.title-annual{left:322px;top:462px;font-size:52px;color:var(--orange)}
.title-velvet{left:279px;top:516px;font-size:86px;color:var(--lavender);text-shadow:0 4px 12px rgba(40,20,120,.6)}
.title-lantern{left:292px;top:612px;font-size:72px;color:var(--green)}
.title-gala{left:381px;top:690px;font-size:84px;color:var(--orange)}
.seal{left:49px;top:625px;width:197px;height:199px;border-radius:50%;
  background:var(--gold);border:10px solid var(--purple);
  display:flex;align-items:center;justify-content:center;text-align:center;
  font-weight:800;font-size:22px;line-height:28px;color:var(--purple)}
.date-line{font-weight:800;text-shadow:0 0 4px rgba(255,255,255,.3)}
.day{left:339px;top:793px;font-size:32px;color:var(--orange)}
.date{left:283px;top:834px;font-size:34px;color:var(--green)}
.time{left:339px;top:884px;font-size:33px;color:var(--royal)}
.at{left:339px;top:927px;font-size:33px;color:var(--royal)}
.venue{left:302px;top:983px;font-weight:800;font-size:22px;line-height:27px;color:var(--orange)}
.address{left:206px;top:1056px;font-weight:700;font-size:22px;line-height:29px;color:var(--green)}
.details{left:651px;top:1020px;width:266px;height:126px;background:var(--white);border-radius:6px;
  padding:18px 12px;font-weight:800;font-size:14.5px;line-height:19px;color:var(--orange);
  box-shadow:0 2px 6px rgba(0,0,0,.3)}
</style>
</head>
<body>
<main class="invitation">
  <div class="brand-mark">KT</div>
  <p class="host">THE ASSOCIATION OF<br>KESTREL TOWER ALUMNI</p>
  <p class="request">REQUESTS<br>YOUR PRESENCE<br>AT OUR</p>
  <span class="edition-number">9</span>
  <span class="edition-suffix">th</span>
  <h1>
    <span class="title title-annual" style="position:absolute">ANNUAL</span>
    <span class="title title-velvet" style="position:absolute">VELVET</span>
    <span class="title title-lantern" style="position:absolute">LANTERN</span>
    <span class="title title-gala" style="position:absolute">GALA</span>
  </h1>
  <div class="seal">KESTREL<br>TOWER</div>
  <p class="date-line day">SATURDAY</p>
  <p class="date-line date">JANUARY 26, 2013</p>
  <p class="date-line time">7PM -12AM</p>
  <p class="date-line at">AT THE</p>
  <p class="venue">HARBORVIEW GRAND<br>CONVENTION HALL</p>
  <p class="address">415 Meridian Plaza Way<br>ATLANTA, GEORGIA</p>
  <p class="details">Cost:$75,00<br>A Semi Format Affair<br>Tuxedos, Dark Suits and Ties<br>NO HATS ALLOWED<br>Tea Lenght or Formal Dresses</p>
</main>
</body>
</html>
```